Under 13 cricket camp

This is a under 13 cricket camp which is sponsored yearly since 1996
"Home of Leo Brandwick U-13 Cricket Cricket Camp"

1. Look at cricket poster 1....logo in the center with batsman and bowler on the sides.

```html
<!DOCTYPE html>
<html lang="en">
<head>
<meta charset="utf-8">
<title>Leo Brandwick U13 Cricket Camp Banner</title>
<link rel="stylesheet" href="https://fonts.googleapis.com/css2?family=Montserrat:wght@600;700;800&family=Oswald:wght@500&display=swap">
<style>
  :root {
    --navy: #0d0f5e;
    --black: #000000;
    --white: #ffffff;
    --backdrop: #c9c9c9;
    --ink: #111111;
  }
  html, body {
    margin: 0;
    padding: 0;
    width: 1200px;
    height: 1200px;
    overflow: hidden;
  }
  body {
    background: radial-gradient(circle at 50% 50%, #eeeeee 0%, var(--backdrop) 75%);
    position: relative;
  }
  .banner {
    position: absolute;
    left: 50%;
    top: 50%;
    width: 1248px;
    height: 620px;
    transform: translate(-50%, -50%) scale(0.8814);
    background: var(--white);
    overflow: hidden;
    box-shadow: 0 6px 24px rgba(0,0,0,0.18);
  }
  .banner-shapes {
    position: absolute;
    inset: 0;
    width: 100%;
    height: 100%;
  }
  .sponsor-mark {
    position: absolute;
    left: 660px;
    top: 70px;
    width: 350px;
    display: flex;
    align-items: center;
    justify-content: center;
    gap: 14px;
    font-family: "Montserrat", sans-serif;
    font-weight: 700;
    font-size: 30px;
    color: var(--navy);
    white-space: nowrap;
  }
  .sponsor-dot {
    width: 34px;
    height: 34px;
    border-radius: 50%;
    background: var(--navy);
    flex: none;
  }
  .camp-home {
    position: absolute;
    left: 514px;
    top: 184px;
    margin: 0;
    font-family: "Montserrat", sans-serif;
    font-weight: 800;
    font-size: 42px;
    letter-spacing: 0.5px;
    line-height: 1.1;
    color: var(--ink);
    white-space: nowrap;
  }
  .camp-age {
    position: absolute;
    left: 505px;
    top: 212px;
    margin: 0;
    font-family: "Montserrat", sans-serif;
    font-weight: 800;
    font-size: 218px;
    line-height: 1;
    letter-spacing: -14px;
    color: var(--navy);
  }
  .camp-label {
    position: absolute;
    left: 893px;
    top: 286px;
    width: 274px;
    height: 114px;
    box-sizing: border-box;
    padding: 6px 0 0 12px;
    background: var(--black);
    color: var(--white);
    font-family: "Montserrat", sans-serif;
    font-weight: 600;
    font-size: 51px;
    line-height: 50px;
    letter-spacing: 1px;
  }
  .sponsor-line {
    position: absolute;
    left: 466px;
    top: 438px;
    margin: 0;
    font-family: "Oswald", sans-serif;
    font-weight: 500;
    font-size: 46px;
    line-height: 80px;
    color: var(--white);
    white-space: nowrap;
    transform: scaleY(1.2);
    transform-origin: left center;
  }
  .web-address {
    position: absolute;
    left: 466px;
    top: 548px;
    margin: 0;
    font-family: "Montserrat", sans-serif;
    font-weight: 700;
    font-size: 42px;
    line-height: 62px;
    letter-spacing: 0.5px;
    color: var(--white);
    white-space: nowrap;
  }
</style>
</head>
<body>
  <section class="banner">
    <svg class="banner-shapes" viewBox="0 0 1248 620" preserveAspectRatio="none">
      <defs>
        <linearGradient id="batsmanTones" x1="0" y1="0" x2="1" y2="1">
          <stop offset="0" stop-color="#f6dcdc"/>
          <stop offset="0.45" stop-color="#f3c9c3"/>
          <stop offset="0.75" stop-color="#cfeef4"/>
          <stop offset="1" stop-color="#d3d6ef"/>
        </linearGradient>
      </defs>
      <rect class="band-navy" x="0" y="418" width="1248" height="122" fill="var(--navy)"/>
      <rect class="band-black" x="0" y="538" width="1248" height="82" fill="var(--black)"/>
      <path class="swoosh-edge" d="M0 0 H345 C485 150 480 440 228 620 H0 Z" fill="var(--navy)"/>
      <path class="swoosh-field" d="M0 0 H334 C452 150 452 440 214 620 H0 Z" fill="var(--white)"/>
      <g role="img" aria-label="Illustration of a batsman in helmet and pads playing a shot at a red cricket ball with a coloured swoosh trail">
        <rect x="20" y="80" width="410" height="525" rx="24" fill="url(#batsmanTones)"/>
      </g>
    </svg>

    <div class="sponsor-mark">
      <span class="sponsor-dot"></span>
      <span class="sponsor-name">Coral Bay Apparel</span>
    </div>

    <h2 class="camp-home">HOME OF LEO BRANDWICK</h2>
    <h1 class="camp-age">U13</h1>
    <div class="camp-label">CRICKET<br>CAMP</div>

    <p class="sponsor-line">SPONSORING YOUTH CRICKET SINCE 1996</p>
    <p class="web-address">WWW.CORALBAYAPPAREL.COM</p>
  </section>
</body>
</html>
```